Flyer-Design für psychologische Beratung und Therapie
Zielgruppe
In meiner Praxis für psychologische Beratung und Therapie unterstütze ich Menschen dabei, ihre Probleme zu lösen. Schwerpunkte sind die Stärkung des Selbstwertgefühls, Überwindung von Ängsten und Krisen.
Aufgabenstellung
Din lang 4-Seitig
(Zitat)
'Bei aller Ernsthaftigkeit und Empathie dürfen Leichtigkeit,
Zuversicht und Humor in der Therapie nicht zu kurz kommen.“
(Text)
Mein Name ist Karl Ewald Lambrecht, ich bin Transaktionsanalytiker, psychotherapeutischer Heilpraktiker und begeisterter VKT® Therapeut. Wenn Sie zufriedener leben wollen, neue Wege einschlagen oder sich beruflich oder persönlich weiterentwickeln wollen, begleite ich Sie gern dabei!
Möchten Sie ein stärkeres Selbstwertgefühl entwickeln, Ängste reduzieren oder eine akute Krise überwinden? Oder geeignete Strategien entwickeln, damit Sie Ihren Beruf zufriedener und erfolgreicher ausüben können? Auf dem Weg zu Ihrem Ziel biete ich Ihnen Unterstützung, vereinbaren Sie gerne einen ersten Termin!

```html
<!DOCTYPE html>
<html lang="de">
<head>
<meta charset="utf-8">
<title>Flyer – Psychologische Beratung &amp; Therapie</title>
<link href="https://fonts.googleapis.com/css2?family=Jost:ital,wght@0,400;0,500;1,400&display=swap" rel="stylesheet">
<style>
  :root{
    --orange:#f39a1e;
    --grey:#6f6f6f;
    --grey-band:#7d7d7d;
    --frame:#a9a9a9;
    --white:#ffffff;
  }
  *{margin:0;padding:0;box-sizing:border-box}
  html,body{width:1200px;height:656px;overflow:hidden;background:var(--white)}
  body{position:relative;font-family:'Jost',sans-serif;color:var(--grey)}
  .panel{position:absolute;top:70px;width:240px;height:480px;border:1px solid var(--frame);overflow:hidden;background:var(--white)}
  .panel--back{left:73px}
  .panel--cover{left:313px}
  .panel--about{left:646px}
  .panel--services{left:886px}
  .panel svg.bg{position:absolute;inset:0}
  .abs{position:absolute}
  .label{position:absolute;top:580px;width:240px;text-align:center;font-size:22px;color:var(--grey)}

  /* Rückseite */
  .back-title{left:32px;top:26px;font-size:17px;font-weight:500}
  .back-intro{left:32px;top:63px;width:196px;font-size:7.6px;line-height:12.8px;color:var(--orange)}
  .back-sub{left:32px;top:153px;width:190px;font-size:10.4px;line-height:14.5px}
  .back-list{left:32px;top:197px;width:196px;list-style:none;font-size:7.6px;line-height:12.8px;color:var(--orange)}
  .back-list li{position:relative;margin-bottom:4.6px}
  .back-list li::before{content:"•";position:absolute;left:-10px}
  .contact-title{left:32px;top:368px;font-size:16px;font-weight:500}
  .contact-col{top:405px;font-size:7.8px;line-height:13px;color:var(--white)}
  .contact-hours{left:32px;top:440px;font-size:7.8px;color:var(--white)}

  /* Cover */
  .brand-dot{left:24px;top:28px;width:24px;height:24px;border-radius:50%;background:var(--orange)}
  .brand-name{left:58px;top:25px;font-size:13.5px;font-weight:500;letter-spacing:.3px;color:var(--grey)}
  .brand-tag{left:58px;top:44px;font-size:9.4px;color:var(--orange)}

  /* Innenteil 3 */
  .quote{right:22px;top:138px;width:170px;text-align:right;font-style:italic;font-size:9.6px;line-height:14.5px}
  .about-bar{left:27px;top:228px;width:4px;height:35px;background:var(--orange)}
  .about-text{left:42px;top:224px;width:180px;font-size:7.6px;line-height:15px;color:var(--orange)}

  /* Innenteil 4 */
  .services-title{left:25px;top:22px;font-size:16.5px;font-weight:500;line-height:20.5px}
  .service{left:0;width:240px;text-align:center}
  .service-icon{display:block;margin:0 auto 6px}
  .service-name{font-size:9.6px;margin-bottom:6px}
  .service-text{font-size:7.6px;line-height:14px;color:var(--orange);padding:0 10px}
</style>
</head>
<body>

<!-- Rückseite -->
<section class="panel panel--back">
  <svg class="bg" width="240" height="480" viewBox="0 0 240 480">
    <polygon points="0,348 240,342 240,360 0,352" fill="var(--grey-band)"/>
    <polygon points="0,352 240,360 240,480 0,480" fill="var(--orange)"/>
  </svg>
  <h2 class="abs back-title">Ich freue mich auf Sie!</h2>
  <p class="abs back-intro">In meiner Privatpraxis können Sie zeitnah Termine vereinbaren. Gesetzliche Krankenversicherungen übernehmen die Kosten in der Regel nicht, Privatversicherte sollten sich vorher bei Ihrem Anbieter erkundigen, inwieweit die Kosten der Behandlung übernommen werden.</p>
  <p class="abs back-sub">Als Selbstzahler haben Sie jedoch zahlreiche Vorteile:</p>
  <ul class="abs back-list">
    <li>Keine Wartezeit, Sie bekommen kurzfristig Termine.</li>
    <li>Sie genießen den Vorteil der absoluten Diskretion, es entfällt die Beantragung der Kostenerstattung und somit eine Dokumentation bei Ihrer Krankenkasse.</li>
    <li>Sie sind nicht an eine bestimmt Frequenz oder bestimmte Anzahl von Therapiestunden gebunden.</li>
    <li>Die Kosten können Sie i.d.R. steuerlich<br>geltend machen.</li>
  </ul>
  <h3 class="abs contact-title">Kontakt</h3>
  <p class="abs contact-col" style="left:32px">Lindenweg 14<br>24117 Kielhusen</p>
  <p class="abs contact-col" style="left:132px">04321 908172<br>info@praxis-lambrecht-demo.de</p>
  <p class="abs contact-hours">Öffnungszeiten nach Absprache!</p>
</section>

<!-- Cover -->
<section class="panel panel--cover">
  <svg class="bg" width="240" height="480" viewBox="0 0 240 480">
    <defs>
      <linearGradient id="coverPhoto" x1="0" y1="0" x2="1" y2="1">
        <stop offset="0" stop-color="#e9ddd0"/>
        <stop offset=".45" stop-color="#b98a66"/>
        <stop offset="1" stop-color="#6f6fa6"/>
      </linearGradient>
    </defs>
    <polygon points="0,76 240,90 240,480 0,480" fill="url(#coverPhoto)" role="img" aria-label="Foto: zwei lachende junge Frauen umarmen sich"/>
    <polygon points="0,66 240,80 240,90 0,76" fill="var(--grey-band)"/>
    <polygon points="88,73 240,69 240,81" fill="var(--orange)"/>
  </svg>
  <span class="abs brand-dot"></span>
  <h1 class="abs brand-name">KARL EWALD LAMBRECHT</h1>
  <p class="abs brand-tag">Psychologische Beratung &amp; Therapie</p>
</section>

<!-- Innenteil 3 -->
<section class="panel panel--about">
  <svg class="bg" width="240" height="480" viewBox="0 0 240 480">
    <defs>
      <radialGradient id="portrait" cx=".5" cy=".45" r=".6">
        <stop offset="0" stop-color="#e6c9b3"/>
        <stop offset=".7" stop-color="#c9d7e6"/>
        <stop offset="1" stop-color="#eef2f6"/>
      </radialGradient>
    </defs>
    <path d="M118,-4 A86,86 0 0 1 152,82" fill="none" stroke="var(--orange)" stroke-width="5"/>
    <path d="M-6,150 A86,86 0 0 0 60,170" fill="none" stroke="#9a9a9a" stroke-width="4"/>
    <circle cx="74" cy="86" r="84" fill="url(#portrait)" role="img" aria-label="Porträtfoto des Therapeuten"/>
  </svg>
  <p class="abs quote">„Bei aller Ernsthaftigkeit und Empathie dürfen Leichtigkeit, Zuversicht und Humor in der Beratung nicht zu kurz kommen.“</p>
  <span class="abs about-bar"></span>
  <p class="abs about-text">Mein Name ist Karl Ewald Lambrecht,<br>ich bin Transaktionsanalytiker, psychotherapeutischer Heilpraktiker, begeisterter VKT®-Therapeut und Puppen-Comedian. Vielleicht ist es mir deshalb so wichtig, dass bei aller Ernsthaftigkeit und Empathie auch Zuversicht, Leichtigkeit und Humor im therapeutischen Prozess nicht zu kurz kommen sollten.<br>Meine Arbeit unterliegt supervisorischer Begleitung. Ich bin den Ethik-Richtlinien des Fachverbands für Transaktionsanalyse (FVTA) verpflichtet. Näheres dazu unter www.fvta-demo.de</p>
</section>

<!-- Innenteil 4 -->
<section class="panel panel--services">
  <h2 class="abs services-title">In diesen Bereichen kann<br>ich Sie unterstützen:</h2>

  <div class="abs service" style="top:82px">
    <svg class="service-icon" width="28" height="28" viewBox="0 0 28 28">
      <circle cx="14" cy="14" r="14" fill="var(--orange)"/>
      <circle cx="14" cy="9" r="3.2" fill="#fff"/>
      <path d="M8,20 Q14,12 20,20 Z" fill="#fff"/>
      <rect x="7" y="19" width="14" height="2.4" fill="#fff"/>
    </svg>
    <p class="service-name">Auftrittscoaching Mentales Training</p>
    <p class="service-text">Reduzieren Sie Ihre Präsentations- oder Prüfungsangst und präsentieren Sie mit Lust und Freude.</p>
  </div>

  <div class="abs service" style="top:177px">
    <svg class="service-icon" width="28" height="28" viewBox="0 0 28 28">
      <circle cx="14" cy="14" r="14" fill="var(--orange)"/>
      <rect x="7.5" y="8" width="13" height="12" rx="1.5" fill="#fff"/>
      <rect x="12.8" y="10.5" width="2.4" height="7" fill="var(--orange)"/>
      <rect x="10.5" y="12.8" width="7" height="2.4" fill="var(--orange)"/>
    </svg>
    <p class="service-name">Entlastung in akuten Krisen</p>
    <p class="service-text">Zur Überbrückung der Wartezeit für eine kassenfinanzierte Psychotherapie biete ich Kurztherapie zur Entlastung.</p>
  </div>

  <div class="abs service" style="top:275px">
    <svg class="service-icon" width="28" height="28" viewBox="0 0 28 28">
      <circle cx="14" cy="14" r="14" fill="var(--orange)"/>
      <circle cx="14" cy="10.5" r="3.8" fill="#fff"/>
      <path d="M7,21 Q14,11 21,21 Z" fill="#fff"/>
    </svg>
    <p class="service-name">Effektive Kurztherapie</p>
    <p class="service-text">Krisen, Ängste, geringes Selbstwertgefühl,<br>Depressionen: Hilfe für mehr Lebenszufriedenheit.</p>
  </div>

  <div class="abs service" style="top:375px">
    <svg class="service-icon" width="28" height="28" viewBox="0 0 28 28">
      <circle cx="14" cy="14" r="14" fill="var(--orange)"/>
      <circle cx="11" cy="10.5" r="3" fill="#fff"/>
      <circle cx="17.5" cy="11.5" r="2.6" fill="#fff"/>
      <path d="M5.5,20 Q11,12 16.5,20 Z" fill="#fff"/>
      <path d="M14,20 Q18,13.5 22.5,20 Z" fill="#fff"/>
    </svg>
    <p class="service-name">Coaching zu beruflichen Anliegen</p>
    <p class="service-text">Ich begleite Sie dabei, beruflich zufriedener und erfolgreicher zu werden.</p>
  </div>
</section>

<p class="label" style="left:73px">Rückseite (2)</p>
<p class="label" style="left:313px">Cover (1)</p>
<p class="label" style="left:646px">Innenteil (3)</p>
<p class="label" style="left:886px">Innenteil (4)</p>

</body>
</html>
```